Meridian Cataract Surgery and Cosmetic Eyelid Surgery

We need Three page website design (home page and interior page template with two looks) with accompanying CSS code. 1. Home page, 2. General Eye-Care page, 3. Cosmetic Eyelid Surgery. #2 an #3 would be only slightly different. See below.

The site being redesigned is http://www.brightlume-vision.com.

The content will remain consistent with the current site.

Additional graphics will be included, especially a number of "Before and after" photos of patients for the various procedures.

You can see competitive sites here: http://www.findora.net/search?q=cosmetic+eyelid+surgury+santa+rosa&ie=utf-8&oe=utf-8&aq=t&client=browser-b&rlz=1R1KKMM_en___US384

The client likes http://www.optiwell-pmc.com, which has a serious look he likes (not necessarily the colors or design). Avoid too many "happy loving couples" and pretty women, on the main page or cataract/general eye-care pages. They are, however, good on the cosmetic pages.

When patients look at the *cosmetic surgery* pages, they can see the pretty women/couples. For *eye surgery* (which is what this is all about) they should see an attractive, active OLDER couple(s) on cataract surgery and refractive surgery pages.

In the US, premium IOL (Intraocular lens - a clear plastic lens that is implanted in the eye; usually done when the natural lens has been removed in a cataract operation) cataract surgery, cosmetic and refractive surgery are not fully paid for by insurance, so patients can afford to pay for it themselves and are more well-off than the normal market.
Updates

Do not use the graphics or look and feel of the current site.  We are looking for a NEW design, not a remix of the old elements.

The new logo is at http://www.pitchforge.net/file.aspx?fileLocation=meridianoptilogo0.jpg

 
Do NOT use the old logo.  If your submitted design uses the old logo, please fix it and delete the one with the old logo.

Sorry for not making this clearer when we started.

Normal 0 false false false EN-US X-NONE X-NONE I want to see a home page that gives equal billing to general eyecare and cosmetic and RECONSTRUCTIVE eyelid surgery.   General eyecare should be listed first.  This should have the correct Practice name and Logo:   Meridian Optical and Cosmetic Eyelid Surgery Center.  The home page should be inviting to both old and young, men and women.  The General eyecare page should have similar appeal.  Cosmetic Page should be decidedly more feminine.  The home page should also highlight Dr. Brennet' s qualification and provide a site map/navigation.

The colors of the logo do not need to be limited to black and white.  The logos MUST be integrated into the design, not just pasted on the page.

Read the brief carefully and pay careful attention to the target markets.

 

Reason: Designs are headed in the right direction, but need more refining.

vector art uploaded:  logo.ai

Reason: Still considering.

Target Market(s)

OLDER men and women. People whose faces, eyes, etc., have an aged look that they want to look younger. ALSO patients who want to have the best possible vision after CATARACT SURGERY. Patients who want Premium IOL'S which give them vision at both distance and near WITHOUT GLASSES. STATE OF THE ART GLAUCOMA SURGERY.

Industry/Entity Type

Plastic

Requirements
Must have
• Easy to read. Some readers may have vision difficulties. Easy to navigate for the elderly market. Cosmetic page may be a little more complex.

```html
<!DOCTYPE html>
<html lang="en">
<head>
<meta charset="utf-8">
<title>Larkspur Valley Eye Care and the Aesthetic Surgery Center</title>
<link href="https://fonts.googleapis.com/css2?family=Arimo:wght@400;700&display=swap" rel="stylesheet">
<style>
:root{
  --black:#000;
  --ink:#222;
  --grey-head:#4a4a4a;
  --blue:#1a72d6;
  --blue-bright:#1d8cf5;
  --blue-deep:#0a3a8c;
  --panel:#fff;
  --menu-grey:#d4d4d4;
  --footer:#111;
  --footer-text:#888;
}
*{margin:0;padding:0;box-sizing:border-box}
html,body{width:689px;height:1200px;overflow:hidden}
body{position:relative;font-family:"Arimo",Arial,sans-serif;color:var(--ink);
  background:linear-gradient(#cfcfcf 278px,#f4f4f4 700px,#fff 1147px)}
.abs{position:absolute}
.header{left:0;top:0;width:689px;height:278px;background:var(--black)}
.header-bar{left:0;top:0;width:689px;height:51px;background:linear-gradient(#111,#2a2a2a);border-bottom:1px solid #3a3a3a}
.nav-divider{top:0;width:1px;height:51px;background:#3c3c3c}
.logo-box{left:36px;top:0;width:188px;height:122px;background:radial-gradient(circle at 50% 45%,#3a8ff5,#0b55d8 75%);display:flex;align-items:center;justify-content:center;gap:6px}
.logo-dot{width:12px;height:12px;border-radius:50%;background:#0a1f66}
.logo-name{font-size:17px;font-weight:400;color:#0a1f66;line-height:1}
.nav-link{top:20px;font-size:9px;color:#fff;letter-spacing:.2px}
.pill{border-radius:10px;background:linear-gradient(#2f9bff,#0656c8);color:#0a2f70;font-size:8px;text-align:center}
.hero-line{left:230px;width:410px;text-align:center;color:#fff}
.hero-small{font-size:14px;color:var(--blue-bright)}
.hero-big{font-size:25px;font-weight:700}
.panel{left:34px;top:278px;width:620px;height:869px;background:var(--panel);box-shadow:0 0 6px rgba(0,0,0,.3)}
.side-btn{left:48px;width:136px;height:28px;background:var(--menu-grey);color:#555;font-size:8.5px;font-weight:700;display:flex;align-items:center;justify-content:center}
.side-btn.active{background:linear-gradient(#2c96ff,#0549b8);color:#fff}
.h-section{font-size:15px;font-weight:700;color:var(--grey-head)}
.body-text{font-size:8.3px;line-height:15px;color:var(--ink)}
.rule{left:59px;top:435px;width:567px;height:1px;background:#d0d0d0}
.bullet{left:90px;width:9px;height:9px}
.link-item{font-size:11.5px;font-weight:700;color:var(--blue)}
.desc{left:141px;font-size:8.2px;color:var(--ink)}
.care-btn{left:97px;width:137px;height:23px;background:linear-gradient(#2f9bff,#06308a);color:#fff;font-size:8.5px;font-weight:700;display:flex;align-items:center;justify-content:center}
.footer{left:0;top:1147px;width:689px;height:53px;background:var(--footer)}
.copyright{left:0;top:1172px;width:689px;text-align:center;font-size:7.5px;color:var(--footer-text)}
</style>
</head>
<body>
<header class="abs header">
  <div class="abs header-bar"></div>
  <div class="abs nav-divider" style="left:444px"></div>
  <div class="abs logo-box"><span class="logo-dot"></span><span class="logo-name">Meridian Optical</span></div>
  <div class="abs pill" style="left:248px;top:18px;width:61px;height:16px;line-height:16px;font-size:8.5px">HOME</div>
  <div class="abs nav-link" style="left:334px">GENERAL EYE-CARE</div>
  <div class="abs nav-link" style="left:465px">COSMETIC EYELID SUGERY</div>
  <div class="abs hero-line hero-small" style="top:84px">WELCOME TO</div>
  <div class="abs hero-line hero-big" style="top:104px">LARKSPUR VALLEY EYE CARE</div>
  <div class="abs hero-line hero-small" style="top:144px">AND THE</div>
  <div class="abs hero-line hero-big" style="top:163px">AESTHETIC SURGERY CENTER</div>
  <div class="abs pill" style="left:546px;top:237px;width:77px;height:21px;line-height:21px">READ MORE</div>
</header>

<main>
  <div class="abs panel"></div>
  <nav>
    <div class="abs side-btn active" style="top:292px">PATIENT PHOTOS</div>
    <div class="abs side-btn" style="top:323px">ABOUT DR. MARTIN BRENNET</div>
    <div class="abs side-btn" style="top:355px">MAP TO OUR OFFICE</div>
    <div class="abs side-btn" style="top:386px">CONTACT US</div>
  </nav>

  <h2 class="abs h-section" style="left:203px;top:310px">OUR MISSION</h2>
  <p class="abs body-text" style="left:205px;top:333px;width:400px">Is to provide personal, friendly, state of the art general eye care as well as the latest advances in cosmetic eyelid surgery for men and women.</p>

  <div class="abs rule"></div>

  <h2 class="abs h-section" style="left:87px;top:460px">EYELID AND FACIAL COSMETIC SURGERY</h2>
  <p class="abs body-text" style="left:61px;top:489px;width:520px;text-indent:24px">Dr Brennet specializes in cosmetic and reconstructive laser surgery of the eyelids and upper face. Because he performs the procedures with super-pulsed carbon dioxide lasers, his patients enjoy less bruising and swelling and are back to work (or play) sooner.</p>
  <p class="abs body-text" style="left:61px;top:571px;width:480px">Dr. Brennet is one of an elite rank of 400 surgeons nationally who are trained in the reconstruction and beautification of eyelids. Following his residency in Ophthalmology, Dr. Brennet was awarded a formal fellowship in eyelid plastic and orbital surgery (One of only 30 nationwide). Is cosmetic eyelid or facial plastic surgery right for you? Enter here to learn more about how cosmetic eyelid surgery can help you.</p>

  <svg width="0" height="0" style="position:absolute">
    <symbol id="target" viewBox="0 0 10 10"><circle cx="5" cy="5" r="3.3" fill="none" stroke="#333" stroke-width="1"/><circle cx="5" cy="5" r="1.4" fill="#333"/><path d="M5 0v2M5 8v2M0 5h2M8 5h2" stroke="#333" stroke-width=".8"/></symbol>
  </svg>
  <svg class="abs bullet" style="top:662px"><use href="#target"/></svg>
  <svg class="abs bullet" style="top:681px"><use href="#target"/></svg>
  <svg class="abs bullet" style="top:700px"><use href="#target"/></svg>
  <svg class="abs bullet" style="top:738px"><use href="#target"/></svg>
  <svg class="abs bullet" style="top:775px"><use href="#target"/></svg>
  <svg class="abs bullet" style="top:813px"><use href="#target"/></svg>

  <div class="abs link-item" style="left:116px;top:661px">Cosmetic Eyelid Surgery For Men and Women</div>
  <div class="abs link-item" style="left:116px;top:680px">How Aesthetic Eyelid Surgery is Performed</div>
  <div class="abs link-item" style="left:126px;top:699px">Upper Eyelids:</div>
  <div class="abs desc" style="top:721px">Advanced laser eyelid surgery precisely removes bulges and wrinkles and allows for less bruising and faster recuperation.</div>
  <div class="abs link-item" style="left:126px;top:737px">Lower Eyelids</div>
  <div class="abs desc" style="top:759px">Bags under eyes can often be removed without visible incisions.</div>
  <div class="abs link-item" style="left:126px;top:775px">Forehead/Brow</div>
  <div class="abs desc" style="top:797px">Endoscopic Brow Lift improves brow/forehead position and contour with only small incisions.</div>
  <div class="abs link-item" style="left:126px;top:812px">Laser Skin Resurfacing</div>
  <div class="abs desc" style="top:835px">Ideal for removing wrinkles around the eyes and mouth. Your complexion looks years younger!</div>

  <h2 class="abs h-section" style="left:72px;top:866px">General Eye Care</h2>
  <p class="abs body-text" style="left:78px;top:888px;width:545px">Martin A. Brennet, MD is certified by the Allied Board of Ophthalmology and is a member of the Guild of Eye Surgeons. He is an expert in the management of cataracts, glaucoma, diabetic retinopathy, dry eye problems and thyroid eye disease. If you would like more information about diseases of the eye and their treatments, look here.</p>

  <div class="abs care-btn" style="top:944px">CATARACTS</div>
  <div class="abs care-btn" style="top:972px">DIABETIC RETIMOPTHY</div>
  <div class="abs care-btn" style="top:1000px">FLASHES AND FLOATERS</div>
  <div class="abs care-btn" style="top:1028px">GLAUCOMA</div>
  <div class="abs care-btn" style="top:1056px">MACULAR DEGENERATION</div>

  <p class="abs body-text" style="left:78px;top:1086px">If you would like to find out more about the office and scheduling appointments</p>
  <div class="abs pill" style="left:440px;top:1102px;width:59px;height:16px;line-height:16px;font-size:6.5px;color:#fff">READ MORE</div>
</main>

<footer>
  <div class="abs footer"></div>
  <p class="abs copyright">Copyright 2010. Larkspur Valley, All rights reserved.</p>
</footer>
</body>
</html>
```